Coastwell Keys Agency Guarantee

We need a flyer to promote a Sydney based property management agency.
We specialise in Property Management on the Northern Beaches of Sydney. A small boutique agency that prides itself on high quality customer service and the lowest fees.
We would like this flyer to promote our listed features in the document provided and focus on our money back guarantee.
The flyer must:
- be designed to match our website www.coastwellkeysagency.com.au
- Contain our logo and contact details
- Use the attached photoshop template for bleed, sizing and fold lines
- final files must include a print ready PDF and fully editable PSD (photoshop) file with included fonts.
Attached are the following files:
Contact details are:
Name: Tom Farrow
Tel: 0491 527 068
email: tom@coastwellkeysagency.com.au
Office: Level 2, 17 Tennerby Rd, Balgowlah NSW 2093
Web: www.coastwellkeysagency.com.au
Target Market(s)
35-75yo Male and Females that own investment properties on Sydney's Norther Beaches
Industry/Entity Type
Real Estate
Requirements
Must have
- The flyer must:
- - Be double sided and colour
- - be designed to match our website www.coastwellkeysagency.com.au
- - Contain our logo and contact details
- - Use the attached photoshop template for bleed, sizing and fold lines
- - final files must include a print ready PDF and fully editable PSD (photoshop) file with included fonts.
Nice to have
- A Money back guarantee "stamp"

```html
<!DOCTYPE html>
<html lang="en">
<head>
<meta charset="utf-8">
<title>Coastwell Keys Agency – Our Guarantee</title>
<link rel="stylesheet" href="https://fonts.googleapis.com/css2?family=Montserrat:wght@400;700&family=Open+Sans:ital,wght@0,400;0,600;1,400&display=swap">
<style>
  :root {
    --navy: #34425a;
    --navy-dark: #2b374c;
    --teal: #1fb5ad;
    --orange: #f26a21;
    --ink: #3a3f47;
    --white: #ffffff;
    --sea-light: #bfe9ef;
    --sea: #33b6cc;
    --sea-deep: #1a6f8c;
    --page: #eceff2;
  }
  * { box-sizing: border-box; margin: 0; padding: 0; }
  html, body {
    width: 1200px; height: 944px; overflow: hidden;
    background: var(--page);
  }
  .brochure {
    position: relative;
    width: 1200px; height: 944px;
    display: flex;
  }
  .panel {
    position: relative;
    width: 400px; height: 944px;
    overflow: hidden;
  }

  /* Cover panel */
  .panel--cover {
    background: var(--navy);
    color: var(--white);
    font-family: "Open Sans", sans-serif;
    padding: 70px 34px 0 34px;
  }
  .cover__rule {
    height: 4px; background: var(--teal); width: 290px;
  }
  .cover__title {
    margin-top: 58px;
    display: inline-block;
    border: 2px solid var(--teal);
    padding: 14px 22px 10px 18px;
    font-family: "Montserrat", sans-serif;
    font-weight: 400;
    line-height: 1;
  }
  .cover__title-small { display: block; font-size: 20px; letter-spacing: 1px; }
  .cover__title-large { display: block; font-size: 46px; letter-spacing: 1px; margin-top: 4px; }
  .cover__copy { margin-top: 26px; }
  .cover__copy p {
    font-size: 12.4px; line-height: 1.5; margin-bottom: 12px;
  }
  .cover__stamp {
    position: absolute; left: 70px; top: 600px;
    width: 220px; height: 220px;
  }
  .cover__note {
    position: absolute; left: 34px; bottom: 52px; right: 60px;
    font-size: 10px; font-style: italic; line-height: 1.45;
  }

  /* Inner panels */
  .panel--inner {
    background: linear-gradient(to bottom, var(--white) 0, var(--white) 430px, var(--sea-light) 640px, var(--sea) 760px);
    font-family: "Open Sans", sans-serif;
    color: var(--ink);
  }
  .panel--inner::before {
    content: ""; position: absolute; left: 0; top: 0; right: 0; height: 22px;
    background: var(--navy);
  }
  .panel--middle { border-left: 6px solid var(--page); }
  .panel--right { border-left: 2px solid var(--page); }
  .harbour-photo {
    position: absolute; left: 0; right: 0; bottom: 0; height: 230px;
    background: linear-gradient(to bottom, #7fc6d8 0%, #a6d2de 30%, #2f8fb0 55%, var(--sea-deep) 100%);
  }
  .features {
    position: relative; z-index: 1;
    padding: 48px 26px 0 22px;
  }
  .feature { margin-bottom: 11px; }
  .feature__title {
    position: relative;
    font-family: "Montserrat", sans-serif;
    font-weight: 700; font-size: 13.2px;
    color: var(--orange); text-transform: uppercase;
    line-height: 1.25; margin-bottom: 2px;
    padding-left: 2px;
  }
  .feature__title::before {
    content: ""; position: absolute; left: -10px; top: 2px;
    border-top: 7px solid var(--navy); border-left: 7px solid transparent;
  }
  .feature p { font-size: 10.8px; line-height: 1.42; }
  .feature p + p { margin-top: 5px; }
  .feature ul { list-style: none; margin-top: 6px; padding-left: 12px; }
  .feature li { position: relative; font-size: 10.8px; line-height: 1.42; margin-bottom: 5px; padding-left: 10px; }
  .feature li::before {
    content: ""; position: absolute; left: 0; top: 6px;
    width: 4px; height: 4px; border-radius: 50%; background: var(--ink);
  }
</style>
</head>
<body>
<main class="brochure">

  <section class="panel panel--cover">
    <div class="cover__rule"></div>
    <h1 class="cover__title">
      <span class="cover__title-small">OUR</span>
      <span class="cover__title-large">GUARANTEE</span>
    </h1>
    <div class="cover__copy">
      <p>At Coastwell Keys Agency we are the Risk Reduction Specialists! Our team will work with you to ensure you're receiving the highest possible return on your investment property. The entire department are heavily focused on maximising your income and optimising capital growth on your investment property.</p>
      <p>We understand when you are selecting a new managing agent it can be a very stressful process for many landlords as you don't know if they are going to deliver on their promises.</p>
      <p>At Coastwell Keys Agency we understand promises can be easily broken and the good news is we GUARANTEE our service.</p>
      <p>If during the first 3 months you are not satisfied with our level of service we promise to you. We are prepared to refund the first 3 months and will give 100% money back on your management fees*</p>
    </div>
    <svg class="cover__stamp" viewBox="0 0 220 220" role="img" aria-label="Orange 100% guarantee stamp">
      <circle cx="110" cy="110" r="100" fill="var(--orange)"/>
      <circle cx="110" cy="110" r="84" fill="none" stroke="var(--white)" stroke-width="3"/>
    </svg>
    <p class="cover__note">*Only applies to management fees. Coastwell Keys Agency must be notified in writing within the 3 month service guarantee period.</p>
  </section>

  <section class="panel panel--inner panel--middle">
    <div class="harbour-photo" role="img" aria-label="Photo of a Sydney harbour bay with moored boats and waterfront homes"></div>
    <div class="features">
      <article class="feature">
        <h2 class="feature__title">Keeping it simple:</h2>
        <p>At the core of our business, we want to keep things simple for you. We understand you have other important things to worry about, so leave your property in the hands of our professional staff, and let them make life easier for you.</p>
      </article>
      <article class="feature">
        <h2 class="feature__title">Senior property manager:</h2>
        <p>The key to any good relationship is people. We have great people that are given the tools needed to manage your property to its full potential.</p>
        <p>Unlike most agencies our focus is property management – not sales. This means we appoint a senior property manager to ensure smooth professional management of your investment.</p>
        <p>Our property managers are not overloaded with hundreds of properties to manage individually. We want to be able to give you and your property the attention they deserve.</p>
      </article>
      <article class="feature">
        <h2 class="feature__title">Strict screening process:</h2>
        <p>All tenancy applications go through a rigorous screening process to ensure we only put forward the best tenants for the landlord's final selection.</p>
        <p>The screening process includes the most up-to-date tenancy database blacklists, financial background checks and employment checks just to list a few.</p>
      </article>
      <article class="feature">
        <h2 class="feature__title">Quality tenant database and corporate re-locators:</h2>
        <p>As we do many openings for properties we get to meet a lot of quality tenants. We take pride in building our database with quality tenants and the type of property they are interested in. It's not uncommon for us to have a screened quality tenant ready to move straight into your property. Ensuring the minimization of untenanted periods.</p>
        <p>We also work closely with corporate re-locators, getting corporate professionals arriving from interstate or internationally into your property.</p>
      </article>
      <article class="feature">
        <h2 class="feature__title">Quick to act and tenant a property:</h2>
        <p>Being a boutique agency, and not overloading our property managers ensures we are able to promptly organize photography, listing and openings to get your property tenanted as quickly as possible with quality tenants.</p>
      </article>
    </div>
  </section>

  <section class="panel panel--inner panel--right">
    <div class="harbour-photo" role="img" aria-label="Photo continuing the harbour bay with yachts and a wooded headland"></div>
    <div class="features">
      <article class="feature">
        <h2 class="feature__title">6 monthly property reports:</h2>
        <p>We go above and beyond when it comes to reports on your property's performance.</p>
        <p>In conjunction with routine inspections every 6 months, we also produce property valuation reports and in-depth Comparative Market Analysis for your property. These reports detail similar properties within close proximity to yours, how they have performed on the market in both sales and rentals. Included in the report are details on the local market in general and how your property has performed, compares and is currently valued at.</p>
      </article>
      <article class="feature">
        <h2 class="feature__title">Landlord portal:</h2>
        <p>At Coastwell Keys Agency we have heavily invested into our cloud-based property management software. With our Landlord Portal, you can log in to download financial reports, live job or maintenance updates as well as detailed photos and videos of your latest inspection. It allows you to stay up-to-date with your property and make sure everything is running the way it should be.</p>
      </article>
      <article class="feature">
        <h2 class="feature__title">Maintenance/renovation plan:</h2>
        <p>Another service we offer is maintenance and renovation plans.</p>
        <p>A common misconception with an investment property is that you want to spend as little as possible on the property, to maximize the yield.</p>
        <p>While our job is to ensure the best financial performance of your property there are two very strong reasons to put together a maintenance/renovation plan for your property.</p>
        <ul>
          <li>Building Equity: Renovations add value to your property, and it might be worth spending $20k on a renovation to increase your properties value up to $60k or more – potentially giving you the equity needed to invest in your next property.</li>
          <li>Ensuring that you aren't ignoring small maintenance issues that could become expensive big problems in the future.</li>
        </ul>
      </article>
    </div>
  </section>

</main>
</body>
</html>
```